Brell Harbor Company Business Cards

Front and Back Business Card - logo and text setup - cool design. I need workable photoshop or illustrator files so I can setup each employee card with design that is created
Updates

Hi everyone, thank you for the great entries. Please no more white and blue cards - there are so many already - black and silver only now please. thanks!

Target Market(s)

Construction Industry - Facility Managers

Industry/Entity Type

Construction

Contact Information for Business Card

I really like contemporary simplistic looks - clean neat....not opposed to seeing some black backrounds

Requirements
Must have
• Logo/website address with design on front only - www.brellharbor-example.com (logo attached)
• Back:
• Name/Title/Company Address/Phone/email address
Nice to have
• Cool design
Should not have
• Nothing gimmicky like Fire or Water - since we are a Fire Protection company - it has all been done

```html
<!DOCTYPE html>
<html lang="en">
<head>
<meta charset="utf-8">
<title>Brell Harbor Company — Business Cards</title>
<link href="https://fonts.googleapis.com/css2?family=Arimo:wght@400;700&display=swap" rel="stylesheet">
<style>
  :root {
    --page: #e8e5e1;
    --charcoal: #403e40;
    --charcoal-deep: #393a36;
    --amber: #db9400;
    --white: #f6f6f7;
    --navy: #2a4a7e;
    --ink: #3a3839;
    --sheen-plum: #8e7388;
    --sheen-cream: #ecdca2;
    --sheen-lilac: #d9c9da;
  }
  html, body {
    margin: 0;
    width: 1200px;
    height: 1200px;
    overflow: hidden;
    background: var(--page);
  }
  .sheet {
    position: relative;
    width: 1200px;
    height: 1200px;
  }
  .card {
    position: absolute;
    left: 150px;
    width: 900px;
    height: 515px;
    box-shadow: 0 10px 24px rgba(0,0,0,0.22);
  }
  .card--back { top: 60px; }
  .card--front { top: 620px; }
  .card svg { display: block; width: 900px; height: 515px; }
  .brand { font-family: "Arimo", Arial, sans-serif; font-weight: 700; fill: var(--navy); }
  .name { font-family: "Arimo", Arial, sans-serif; font-weight: 700; font-size: 40px; fill: var(--white); }
  .role { font-family: "Arimo", Arial, sans-serif; font-weight: 400; font-size: 27px; fill: var(--amber); }
  .address { font-family: "Arimo", Arial, sans-serif; font-weight: 400; font-size: 24px; fill: var(--ink); }
  .contact { font-family: "Arimo", Arial, sans-serif; font-weight: 400; font-size: 17px; fill: var(--white); }
  .web-front { font-family: "Arimo", Arial, sans-serif; font-weight: 400; font-size: 22px; fill: var(--amber); }
</style>
</head>
<body>
<main class="sheet">

  <!-- Back: personal details -->
  <section class="card card--back" aria-label="Business card, contact side">
    <svg viewBox="0 0 900 515" xmlns="http://www.w3.org/2000/svg">
      <defs>
        <linearGradient id="sheen-back" x1="0" y1="0" x2="1" y2="0">
          <stop offset="0" stop-color="var(--sheen-plum)"/>
          <stop offset="0.4" stop-color="var(--sheen-cream)"/>
          <stop offset="0.75" stop-color="var(--sheen-lilac)"/>
          <stop offset="1" stop-color="var(--sheen-plum)"/>
        </linearGradient>
        <linearGradient id="fold-shade-back" x1="0.62" y1="0.6" x2="0.5" y2="0.47" gradientUnits="objectBoundingBox">
          <stop offset="0" stop-color="#2e2b2e" stop-opacity="0.85"/>
          <stop offset="1" stop-color="#2e2b2e" stop-opacity="0"/>
        </linearGradient>
      </defs>
      <rect class="card-base" width="900" height="515" fill="var(--charcoal)"/>
      <polygon class="sheen-panel" points="0,0 500,0 0,470" fill="url(#sheen-back)"/>
      <polygon class="sheen-fold" points="500,0 0,470 0,400 430,0" fill="url(#fold-shade-back)" opacity="0.7"/>
      <polygon class="amber-wedge" points="640,0 900,0 900,95 545,95" fill="var(--amber)"/>
      <polygon class="amber-band" points="400,215 900,215 900,395 150,395" fill="var(--amber)"/>

      <text class="brand" x="50" y="115" font-size="32">Brell Harbor</text>
      <text class="brand" x="50" y="152" font-size="32">Company</text>

      <text class="name" x="862" y="150" text-anchor="end">NAME SURNAME</text>
      <text class="role" x="862" y="182" text-anchor="end">MANAGER</text>
      <text class="address" x="862" y="258" text-anchor="end">Adress. Street. number</text>
      <text class="address" x="862" y="292" text-anchor="end">City CODE</text>

      <g class="icon icon--mail" transform="translate(195,395)">
        <circle r="23" fill="var(--white)"/>
        <rect x="-12" y="-8" width="24" height="16" rx="2" fill="var(--amber)"/>
        <polyline points="-12,-8 0,2 12,-8" fill="none" stroke="var(--white)" stroke-width="2"/>
      </g>
      <g class="icon icon--web" transform="translate(475,395)">
        <circle r="23" fill="var(--white)"/>
        <g fill="none" stroke="var(--amber)" stroke-width="2">
          <circle r="13"/>
          <ellipse rx="6" ry="13"/>
          <line x1="-13" y1="0" x2="13" y2="0"/>
          <line x1="-11" y1="-7" x2="11" y2="-7"/>
          <line x1="-11" y1="7" x2="11" y2="7"/>
        </g>
      </g>
      <g class="icon icon--phone" transform="translate(765,395)">
        <circle r="23" fill="var(--white)"/>
        <rect x="-7" y="-12" width="14" height="24" rx="3" fill="none" stroke="var(--amber)" stroke-width="2.4"/>
        <circle cx="0" cy="7" r="1.6" fill="var(--amber)"/>
      </g>

      <text class="contact" x="195" y="465" text-anchor="middle">contact@brellharbor-example.com</text>
      <text class="contact" x="475" y="465" text-anchor="middle">www.brellharbor-example.com</text>
      <text class="contact" x="765" y="465" text-anchor="middle">+33 333 333 333</text>
    </svg>
  </section>

  <!-- Front: company name and website -->
  <section class="card card--front" aria-label="Business card, company side">
    <svg viewBox="0 0 900 515" xmlns="http://www.w3.org/2000/svg">
      <defs>
        <linearGradient id="sheen-front" x1="0" y1="0" x2="1" y2="0">
          <stop offset="0" stop-color="var(--sheen-plum)"/>
          <stop offset="0.35" stop-color="var(--sheen-cream)"/>
          <stop offset="0.7" stop-color="var(--sheen-lilac)"/>
          <stop offset="1" stop-color="var(--sheen-plum)"/>
        </linearGradient>
        <linearGradient id="fade-white" x1="0" y1="0" x2="1" y2="0">
          <stop offset="0" stop-color="var(--white)" stop-opacity="0"/>
          <stop offset="0.22" stop-color="var(--white)" stop-opacity="1"/>
          <stop offset="1" stop-color="var(--white)" stop-opacity="1"/>
        </linearGradient>
      </defs>
      <rect class="card-base" width="900" height="515" fill="var(--charcoal-deep)"/>
      <polygon class="sheen-panel" points="0,0 540,0 0,260" fill="url(#sheen-front)"/>
      <polygon class="amber-wedge" points="740,0 900,0 900,120 500,120" fill="var(--amber)"/>
      <polygon class="white-band" points="150,120 900,120 900,290 0,290" fill="url(#fade-white)"/>
      <polygon class="amber-band" points="300,290 900,290 900,420 80,420" fill="var(--amber)"/>

      <text class="brand" x="860" y="222" font-size="50" text-anchor="end">Brell Harbor Company</text>

      <g class="icon icon--web" transform="translate(450,455)" fill="none" stroke="var(--amber)" stroke-width="2.2">
        <circle r="14"/>
        <ellipse rx="6.5" ry="14"/>
        <line x1="-14" y1="0" x2="14" y2="0"/>
        <line x1="-12" y1="-7" x2="12" y2="-7"/>
        <line x1="-12" y1="7" x2="12" y2="7"/>
      </g>
      <text class="web-front" x="450" y="498" text-anchor="middle">www.brellharbor-example.com</text>
    </svg>
  </section>

</main>
</body>
</html>
```